Reboot of current Powerpoint Design

We would like to modernise our current powerpoint design which we use for the delivery of class room based training to 5-10 trainees at a time. We have attached our current design but would like a more updated (yet still practical for in-house edits and development).
We would like to be left with a collection of no more than 10-20 master slides for ongoing use in the business. Critically the slides should be focussed on being able to be easily read in a classroom environment, have minimal or no animation (easy to operate by a trainer) and should recognise our customer base which is largely fairly conservative (heavy industry).
In short we are seeking a professional and engaging end result which mirrors our current branding.
Across our entire range of courses we will use the following key structure:
- Title
- Introductory slides
- Overviews
- Modules
- Content
- Discussion
- Conclusion
As part of this update we would like to increase our use of photos (noting that we are not limited to the photos in the current powerpoint so any design should simply use placeholders).
The updated version should incorporate our current branding which is represented in the attached example powerpoint as well as our website (www.brightlaneskills.com).
Thanks
Glen
Updates
Target Market(s)
Safety and compliance in heavy industries (eg. mining, manufacturing, construction, etc.)
Industry/Entity Type
Training
Font styles to use
Other font styles liked:
- Helvetica (or similar to be used on windows machines)
Colors
Designer to choose colors to be used in the design.
Requirements
Must have
- Approximately 20 master slides that can be easily applied across a large number of current power point presentations.
- Strong visual focus with main use in classroom environment (so note that these are used on a projector screen - please take into account (eg. no small fonts).
- We generally use the notes section for any detailed information (trainer benefit) so our focus is on using the slides as triggers for conversations, training structure and headline topics.
- If anything we are focussed on a less is more mentality and are looking for a clean, simple and professional appeal. Note we have no issue in some of the content of the example slides (CPR) moving to the notes section.
- We have also just begun implementing a new brand bi-line which is:
- PlanWell. MoveWell. BuildWell. (Note the Safe. in each word is in BOLD).
- This bi-line needs to be incorporated along with the Brightlane Skills logo in each slide. Please note that we also use the unique A design in the Brightlane Skills logo as a further design feature in our branding documents. As per current powerpoint, we would prefer this to be incorporated as well.
Nice to have
- Functional graphics (easy to edit) and branded icons to ensure we continue to push the Brightlane Skills brand throughout the presentations.
Should not have
- Animation and difficult to edit slides.

```html
<!DOCTYPE html>
<html lang="en">
<head>
<meta charset="utf-8">
<title>Brightlane Skills – Training Master Slides</title>
<link href="https://fonts.googleapis.com/css2?family=Roboto:wght@300;400;700;900&display=swap" rel="stylesheet">
<style>
:root{
  --red:#c8202f;
  --red-dark:#9e1522;
  --ink:#2b2b2b;
  --grey:#8a8a8a;
  --line:#d9d9d9;
  --canvas:#e9e9e9;
  --paper:#ffffff;
  --gold:#c9a86a;
}
*{box-sizing:border-box;margin:0;padding:0}
html,body{width:853px;height:1200px;overflow:hidden;background:var(--canvas);font-family:"Roboto",Helvetica,Arial,sans-serif;color:var(--ink)}
.slide{position:absolute;width:385px;height:182px;background:var(--paper);overflow:hidden;box-shadow:0 1px 3px rgba(0,0,0,.15)}
.col-a{left:34px}.col-b{left:434px}
.row-1{top:8px}.row-2{top:205px}.row-3{top:402px}.row-4{top:599px}.row-5{top:796px}.row-6{top:993px}
.slide-title{position:absolute;left:16px;top:12px;font-size:12px;font-weight:700;color:var(--ink)}
.slide-title span{font-weight:300;color:var(--grey)}
.mini-brand{position:absolute;right:14px;top:13px;font-size:5px;font-weight:700;letter-spacing:.5px;color:var(--ink)}
.footer{position:absolute;left:0;right:0;bottom:0;height:10px;border-top:1px solid var(--line);font-size:3.5px;color:var(--grey);text-align:center;line-height:9px}
.footer::before{content:"";position:absolute;left:0;top:-1px;width:70px;height:2px;background:var(--red)}
.brand{font-weight:900;color:var(--ink);letter-spacing:.5px;line-height:1}
.stripes{position:absolute;display:flex;gap:2px}
.stripes i{display:block;width:3px}
.photo{position:absolute}
.body{font-size:4.5px;line-height:1.6;color:#555}
.num{font-size:13px;font-weight:700;color:var(--red);line-height:1}
.item{position:absolute;width:70px}
.item .rule{height:1px;background:var(--line);margin:3px 0}
.item h4{font-size:5px;font-weight:700;color:var(--ink)}
.list-row{display:flex;align-items:center;gap:8px;border-bottom:1px solid var(--line);height:13px;font-size:5px}
.list-row b{color:var(--red);width:10px}
.list-row em{font-style:normal;margin-left:auto;color:var(--grey)}
</style>
</head>
<body>

<!-- 1 Title -->
<section class="slide col-a row-1">
  <div class="photo" role="img" aria-label="Faint construction site skyline with cranes" style="right:0;top:0;width:230px;height:110px;background:linear-gradient(180deg,#f4f4f4,#e6e6e6)"></div>
  <div class="stripes" style="left:0;top:0;height:182px">
    <i style="background:var(--red);height:182px"></i><i style="background:#555;height:182px"></i><i style="background:#bbb;height:182px"></i>
  </div>
  <div style="position:absolute;left:30px;top:92px">
    <div class="brand" style="font-size:15px">BRIGHTLANE<br><span style="font-size:9px">SKILLS</span></div>
    <div style="font-size:10px;font-weight:700;margin-top:6px">Provide Cardiopulmonary Resuscitation</div>
    <div style="font-size:5px;color:var(--grey);margin-top:3px">PlanWell. MoveWell. BuildWell.</div>
  </div>
  <div class="footer">www.brightlaneskills.com</div>
</section>

<!-- 2 Course overview -->
<section class="slide col-b row-1">
  <div class="slide-title">Course <span>overview</span></div>
  <div class="mini-brand">BRIGHTLANE SKILLS</div>
  <div style="position:absolute;left:120px;top:42px;width:150px">
    <div class="list-row"><b>1</b>Introduction &amp; housekeeping</div>
    <div class="list-row" style="color:var(--grey)">Course aims and outcomes</div>
    <div class="list-row"><b>2</b>Assessment requirements</div>
    <div class="list-row" style="color:var(--grey)">Practical tasks and questions</div>
    <div class="list-row"><b>3</b>Emergency response</div>
    <div class="list-row" style="color:var(--grey)">Perform CPR procedures</div>
  </div>
  <div class="footer">PlanWell. MoveWell. BuildWell.</div>
</section>

<!-- 3 Section list -->
<section class="slide col-a row-2">
  <div class="mini-brand">BRIGHTLANE SKILLS</div>
  <div class="stripes" style="left:0;top:0">
    <i style="background:var(--red);height:182px"></i><i style="background:#555;height:182px"></i><i style="background:#bbb;height:182px"></i>
  </div>
  <div style="position:absolute;left:100px;top:40px;width:200px">
    <div class="list-row" style="font-weight:700;color:var(--red)">Introduction &amp; housekeeping</div>
    <div class="list-row">Recognise an emergency situation<em>01</em></div>
    <div class="list-row">Assess the scene for hazards<em>02</em></div>
    <div class="list-row">Check for response and breathing<em>03</em></div>
    <div class="list-row">Call for help and an AED<em>04</em></div>
    <div class="list-row">Begin compressions and breaths<em>05</em></div>
  </div>
  <div class="footer">PlanWell. MoveWell. BuildWell.</div>
</section>

<!-- 4 Quote -->
<section class="slide col-b row-2">
  <div class="slide-title">Quote <span>Name</span></div>
  <div class="mini-brand">BRIGHTLANE SKILLS</div>
  <div style="position:absolute;left:0;right:0;top:40px;text-align:center">
    <div style="font-size:30px;font-weight:900;color:var(--red);line-height:.6">&ldquo;</div>
    <div style="font-size:15px;line-height:1.25;margin-top:8px">Any attempt at<br>resuscitation is better<br>than no attempt</div>
    <div style="font-size:30px;font-weight:900;color:var(--red);line-height:.6;margin-top:12px">&rdquo;</div>
  </div>
  <div class="footer">PlanWell. MoveWell. BuildWell.</div>
</section>

<!-- 5 Section divider -->
<section class="slide col-a row-3">
  <div style="position:absolute;left:0;top:0;width:385px;height:60px;background:linear-gradient(180deg,#f6f6f6,#fff)"></div>
  <div class="stripes" style="left:0;top:100px">
    <i style="background:var(--red);height:82px"></i><i style="background:#555;height:82px"></i><i style="background:#bbb;height:82px"></i>
  </div>
  <div style="position:absolute;left:18px;top:118px;display:flex;align-items:center;gap:14px">
    <div class="brand" style="font-size:12px">BRIGHTLANE<br><span style="font-size:7px">SKILLS</span></div>
    <div style="width:1px;height:24px;background:var(--line)"></div>
    <div>
      <div style="font-size:12px;font-weight:700">Perform CPR procedures</div>
      <div style="font-size:5px;color:var(--grey)">Module one – scene and response</div>
    </div>
  </div>
  <div class="footer">www.brightlaneskills.com</div>
</section>

<!-- 6 Emergency response: photo + text -->
<section class="slide col-b row-3">
  <div class="slide-title">Emergency <span>Response</span></div>
  <div class="mini-brand">BRIGHTLANE SKILLS</div>
  <div class="photo" role="img" aria-label="Photo of a trainee performing chest compressions on a manikin" style="left:16px;top:34px;width:95px;height:112px;background:linear-gradient(160deg,#b7402f,#6e2a22)"></div>
  <div style="position:absolute;left:16px;top:140px;width:95px;height:10px;background:var(--red);color:#fff;font-size:4px;line-height:10px;text-align:center">Scene safety first</div>
  <div style="position:absolute;left:125px;top:38px;width:240px">
    <div style="font-size:6px;font-weight:700">Respond to an<br>emergency situation</div>
    <p class="body" style="margin-top:5px">Check the area for danger to yourself, bystanders and the casualty before you approach. Remove hazards where it is safe to do so.</p>
    <p class="body" style="margin-top:3px">Look for a response, open the airway and check breathing for no more than ten seconds.</p>
    <p class="body" style="margin-top:3px">Call emergency services or send a bystander to call and fetch an AED.</p>
    <p class="body" style="margin-top:3px">Start compressions promptly and continue until help arrives.</p>
  </div>
  <div class="footer">PlanWell. MoveWell. BuildWell.</div>
</section>

<!-- 7 Emergency response: red photo + numbers -->
<section class="slide col-a row-4">
  <div class="slide-title">Emergency <span>Response</span></div>
  <div class="mini-brand">BRIGHTLANE SKILLS</div>
  <div class="photo" role="img" aria-label="Red-toned photo of hands performing CPR" style="left:16px;top:34px;width:225px;height:128px;background:linear-gradient(135deg,#d24a4a,#8e1d22)"></div>
  <div style="position:absolute;left:36px;top:52px;width:110px;background:rgba(255,255,255,.9);padding:7px">
    <div style="font-size:6px;font-weight:700;color:var(--red)">Respond to an<br>emergency situation</div>
    <p class="body" style="margin-top:3px">Stay calm, check for danger and assess the casualty before you act.</p>
  </div>
  <div style="position:absolute;left:260px;top:38px;width:110px">
    <div class="num">01</div><p class="body">Check for danger</p>
    <div class="num" style="margin-top:6px">02</div><p class="body">Send for help</p>
    <div class="num" style="margin-top:6px">03</div><p class="body">Start compressions</p>
  </div>
  <div class="footer">PlanWell. MoveWell. BuildWell.</div>
</section>

<!-- 8 Emergency response: 4 items + photo -->
<section class="slide col-b row-4">
  <div class="slide-title">Emergency <span>Response</span></div>
  <div class="mini-brand">BRIGHTLANE SKILLS</div>
  <div style="position:absolute;left:16px;top:34px;width:130px">
    <div style="font-size:6px;font-weight:700">Respond to an emergency</div>
    <p class="body">Follow the four steps below in order.</p>
  </div>
  <div class="item" style="left:16px;top:66px"><div class="num">01</div><div class="rule"></div><h4>Danger</h4><p class="body">Check the scene is safe.</p></div>
  <div class="item" style="left:100px;top:66px"><div class="num">02</div><div class="rule"></div><h4>Response</h4><p class="body">Talk and touch gently.</p></div>
  <div class="item" style="left:16px;top:116px"><div class="num">03</div><div class="rule"></div><h4>Send</h4><p class="body">Call for help now.</p></div>
  <div class="item" style="left:100px;top:116px"><div class="num">04</div><div class="rule"></div><h4>Airway</h4><p class="body">Open and check it.</p></div>
  <div class="photo" role="img" aria-label="Photo of workers in hard hats giving CPR on site" style="left:190px;top:30px;width:195px;height:142px;background:linear-gradient(150deg,#b99a7a,#5b4a3c)"></div>
  <div class="footer">PlanWell. MoveWell. BuildWell.</div>
</section>

<!-- 9 Emergency response: centre figure -->
<section class="slide col-a row-5">
  <div class="slide-title">Emergency <span>Response</span></div>
  <div class="mini-brand">BRIGHTLANE SKILLS</div>
  <div class="photo" role="img" aria-label="Cut-out photo of a rescuer giving CPR to a person lying down" style="left:140px;top:44px;width:105px;height:100px;border-radius:50%;background:radial-gradient(circle,#d8d8d8,#fff 70%)"></div>
  <svg style="position:absolute;left:0;top:0" width="385" height="182" aria-hidden="true">
    <g stroke="#cfcfcf" stroke-width=".8" fill="none">
      <path d="M110 60 L145 80"/><path d="M110 130 L145 112"/><path d="M275 60 L240 80"/><path d="M275 130 L240 112"/>
    </g>
  </svg>
  <div class="item" style="left:30px;top:40px"><div class="num">01</div><p class="body">Check for danger</p></div>
  <div class="item" style="left:30px;top:110px"><div class="num">02</div><p class="body">Check response</p></div>
  <div class="item" style="left:285px;top:40px"><div class="num">03</div><p class="body">Open the airway</p></div>
  <div class="item" style="left:285px;top:110px"><div class="num">04</div><p class="body">Start compressions</p></div>
  <div class="footer">PlanWell. MoveWell. BuildWell.</div>
</section>

<!-- 10 Perform procedure -->
<section class="slide col-b row-5">
  <div class="slide-title">Perform <span>Procedure</span></div>
  <div class="mini-brand">BRIGHTLANE SKILLS</div>
  <svg style="position:absolute;left:0;top:0" width="385" height="182" aria-hidden="true">
    <path d="M50 95 C80 55,120 55,140 95 S200 135,230 95 S290 55,330 95" stroke="var(--red)" stroke-width="4" fill="none"/>
    <circle cx="60" cy="95" r="17" fill="var(--gold)"/>
    <circle cx="140" cy="95" r="17" fill="var(--gold)"/>
    <circle cx="230" cy="95" r="17" fill="var(--gold)"/>
    <circle cx="320" cy="95" r="17" fill="var(--gold)"/>
  </svg>
  <div class="item" style="left:82px;top:118px"><div class="num">01</div><p class="body">Check the scene</p></div>
  <div class="item" style="left:110px;top:44px"><div class="num">02</div><p class="body">Call for help</p></div>
  <div class="item" style="left:252px;top:118px"><div class="num">03</div><p class="body">Give 30 compressions</p></div>
  <div class="item" style="left:290px;top:36px"><div class="num">04</div><p class="body">Give 2 breaths</p></div>
  <p class="body" style="position:absolute;left:40px;right:40px;top:148px;text-align:center">Repeat the cycle of compressions and breaths until help arrives or the casualty recovers.</p>
  <div class="footer">PlanWell. MoveWell. BuildWell.</div>
</section>

<!-- 11 Thank you -->
<section class="slide col-a row-6" style="width:385px">
  <div style="position:absolute;left:0;top:0;width:385px;height:60px;background:linear-gradient(180deg,#f6f6f6,#fff)"></div>
  <div class="stripes" style="left:0;top:100px">
    <i style="background:var(--red);height:82px"></i><i style="background:#555;height:82px"></i><i style="background:#bbb;height:82px"></i>
  </div>
  <div style="position:absolute;left:18px;top:118px;display:flex;align-items:center;gap:14px">
    <div class="brand" style="font-size:12px">BRIGHTLANE<br><span style="font-size:7px">SKILLS</span></div>
    <div style="width:1px;height:24px;background:var(--line)"></div>
    <div>
      <div style="font-size:14px;font-weight:700">Thank You</div>
      <div style="font-size:5px;color:var(--grey)">www.brightlaneskills.com</div>
    </div>
  </div>
  <div class="footer">PlanWell. MoveWell. BuildWell.</div>
</section>

<!-- 12 Closing -->
<section class="slide col-b row-6">
  <div class="slide-title">Emergency <span>Response</span></div>
  <div class="mini-brand">BRIGHTLANE SKILLS</div>
  <div style="position:absolute;left:16px;top:40px;width:350px">
    <div class="list-row"><b>01</b>Review key steps of the CPR cycle</div>
    <div class="list-row"><b>02</b>Practise on the training manikin</div>
    <div class="list-row"><b>03</b>Complete the written assessment</div>
  </div>
  <div class="footer">PlanWell. MoveWell. BuildWell.</div>
</section>

</body>
</html>
```